New Business Card for Casual Beachfront Cafe

Quirky Beachfront Cafe at Moana, South Australia needs a DOUBLE SIDED business card to print on PrintHarbor.

Target Market(s)

Business Cards sit on the counter for Guests to take with them. Please view our website www.saltreefcafe.com.au to get a feel for the Cafe. You may also view our Instagram at @saltreefcafe

Industry/Entity Type

Cafe / Restaurant

Contact Information for Business Card

Information equivalent to: Breakfast, Lunch, Dinner, Coffee, Takeaway / 117 Parade Tidemere SA 5174 / Menu & Opening Hours: www.saltreefcafe.com.au / ph (08) 8461 9273

Requirements
Must have
• Information equivalent to: Breakfast, Lunch, Dinner, Coffee, Takeaway / 117 Parade Tidemere SA 5174 / Menu & Opening Hours: www.saltreefcafe.com.au / ph (08) 8461 9273
Nice to have
• Potentially some of our trademark colours (Cafe can be searched via Seekly)
Should not have
• Must NOT have image of the building. May have the logo provided on one side but not necessarily, depending on how you wish to design the card

```html
<!DOCTYPE html>
<html lang="en">
<head>
<meta charset="utf-8">
<title>Salt Reef Cafe – Business Card</title>
<link href="https://fonts.googleapis.com/css2?family=Montserrat:wght@400;500;700;800&display=swap" rel="stylesheet">
<style>
  :root {
    --backdrop: #e9e6e1;
    --card: #3b5f63;
    --accent: #f2e600;
    --ink-light: #eef3f3;
    --shadow: rgba(0, 0, 0, 0.35);
  }
  * { margin: 0; padding: 0; box-sizing: border-box; }
  html, body {
    width: 900px;
    height: 1200px;
    overflow: hidden;
    background: var(--backdrop);
    font-family: "Montserrat", sans-serif;
  }
  .canvas { position: relative; width: 900px; height: 1200px; }

  .card {
    position: absolute;
    left: 78px;
    width: 744px;
    height: 442px;
    background: var(--card);
    border-radius: 40px;
    box-shadow: 0 6px 14px var(--shadow);
  }
  .card--front { top: 130px; }
  .card--back { top: 638px; height: 440px; }

  .brand-name {
    position: absolute;
    display: flex;
    align-items: center;
    justify-content: center;
    gap: 16px;
    color: var(--accent);
    font-weight: 800;
    text-transform: uppercase;
    letter-spacing: 1px;
    line-height: 1.05;
    text-align: center;
  }
  .brand-name__mark {
    width: 14px;
    height: 14px;
    background: var(--accent);
    flex: none;
  }
  .card--front .brand-name { left: 42px; top: 134px; width: 328px; height: 176px; font-size: 44px; }
  .card--back .brand-name { left: 100px; top: 74px; width: 548px; height: 294px; font-size: 76px; gap: 24px; }
  .card--back .brand-name__mark { width: 22px; height: 22px; }

  .divider {
    position: absolute;
    left: 395px;
    top: 92px;
    width: 2px;
    height: 260px;
    background: var(--accent);
  }

  .details { position: absolute; left: 422px; top: 96px; color: var(--ink-light); }
  .person-name {
    color: var(--accent);
    font-size: 29px;
    font-weight: 700;
    letter-spacing: 0.6px;
    line-height: 1;
  }
  .person-role { font-size: 18px; margin-top: 10px; }

  .contact-list { list-style: none; margin-top: 28px; }
  .contact-list li {
    display: flex;
    align-items: center;
    gap: 6px;
    font-size: 18px;
    height: 29.5px;
  }
  .contact-icon { width: 17px; height: 17px; flex: none; }

  .address { font-style: normal; font-size: 18px; line-height: 29px; margin-top: 22px; }

  .services {
    position: absolute;
    left: 0;
    right: 0;
    top: 380px;
    text-align: center;
    color: var(--ink-light);
    font-size: 19px;
  }
</style>
</head>
<body>
<main class="canvas">

  <section class="card card--front" aria-label="Business card front">
    <div class="brand-name"><span class="brand-name__mark"></span><span>Salt Reef<br>Cafe</span></div>
    <div class="divider"></div>
    <div class="details">
      <h1 class="person-name">MARCUS HALE</h1>
      <p class="person-role">Managing Director</p>
      <ul class="contact-list">
        <li>
          <svg class="contact-icon" viewBox="0 0 20 20" aria-hidden="true">
            <path fill="#f2e600" d="M2 7c0-3 3-4 8-4s8 1 8 4v1h-4V6.5c-1-.6-7-.6-8 0V8H2z M5 9l2-2h6l2 2 2 7H3z"/>
            <circle cx="10" cy="12.5" r="2" fill="#3b5f63"/>
          </svg>
          (08) 8461 9273
        </li>
        <li>
          <svg class="contact-icon" viewBox="0 0 20 20" aria-hidden="true">
            <rect x="3" y="3" width="14" height="14" fill="#f2e600"/>
          </svg>
          @saltreefcafe
        </li>
        <li>
          <svg class="contact-icon" viewBox="0 0 20 20" aria-hidden="true">
            <circle cx="10" cy="10" r="7.5" fill="none" stroke="#f2e600" stroke-width="2"/>
            <ellipse cx="10" cy="10" rx="3" ry="7.5" fill="none" stroke="#f2e600" stroke-width="1.5"/>
            <line x1="2.5" y1="10" x2="17.5" y2="10" stroke="#f2e600" stroke-width="1.5"/>
          </svg>
          www.saltreefcafe.com.au
        </li>
      </ul>
      <address class="address">117 Parade<br>Tidemere SA 5174</address>
    </div>
    <p class="services">Breakfast, Lunch, Dinner, Coffee, Takeaway</p>
  </section>

  <section class="card card--back" aria-label="Business card back">
    <div class="brand-name"><span class="brand-name__mark"></span><span>Salt Reef<br>Cafe</span></div>
  </section>

</main>
</body>
</html>
```